Natural Handmade Cosmetics Line

I'm looking for a range of labels for a natural handmade Cosmetics company in UK. I'm looking to print the labels on a transparent substrate. The ingredients & Details are on the website. Vorenta means Lovely or beloved in latin. The products are designed & manufactured by hand but I want to give the impression of a high end cosmetic brand.

I would like a tag line of some description like "Natural, Pure, Handmade" included

The name of the company is vorenta cosmetics (www.vorenta.co.uk) and I have the following products (All skin types)

1. Orange & Rose Toner - 150ml (Length: 14cm / hight 9.5cm)
2. Grapefruit Cleanser - 150g (Length 14cm / Hight 9.5cm)
3. Balancing Facial Oil - 30ml (Length 10.5cm / Hight 4.6cm)
4. Frankincense & Neroli Facial Oil - 30ml (Length 10.5cm / Hight 4.6cm)
5. Neroli Moisturizing Face Cream - 50g (Length 15cm / Hight 5cm)
6. Lavender & Neroli Hand Cream - 100g (Length 15cm / Hight 8cm)
7. Tangerine Lip Balm - 4g (Length 5.4cm / Hight 4.6cm) - Lip Balm Tube
8. Mandarin Treatment Balm 50g (Length16.4cm / Hight 3.1cm)
9. Lemon & Tangerine Body Butter - 100g (Length 29cm / Hight 2.5cm)
10. Ylang Ylang & Bergamot Body Butter - 100g (Length 29cm / Hight 2.5cm)

Ideally in the future I would like to get some boxes designed.

I like the following designs

https://www.kestrova.co.uk/face/range/product-family/daily-essentials/
http://www.tolvanhue.co.uk/shop-for-products/natural-skin-care/organic-moisturiser-products
http://www.quobaskincare.com/
http://www.lumiskincare.com/
http://www.brindlemoorwellness.co.uk/organic-natural-skincare/dry-sensitive/lumiskincare-daily-moisture-for-men.html
Updates

Dimensions altered

Target Market(s)

Targeting woman of 25+

Industry/Entity Type

Cosmetics

Requirements
Must have
• The correct symbols which are included

```html
<!DOCTYPE html>
<html lang="en">
<head>
<meta charset="utf-8">
<title>Vorenta Orange &amp; Rose Toner Label</title>
<link href="https://fonts.googleapis.com/css2?family=Prata&family=Montserrat:wght@400;500;700&display=swap" rel="stylesheet">
<style>
  :root {
    --backdrop: #ececec;
    --label: #ffffff;
    --ink: #1f1f1f;
    --orange: #f39200;
    --rose: #e2195b;
    --citrus-light: #ffd23f;
    --citrus-deep: #f08a00;
    --petal-light: #f7c1d0;
    --petal-deep: #e07a99;
  }
  * { margin: 0; padding: 0; box-sizing: border-box; }
  html, body {
    width: 1035px;
    height: 1200px;
    overflow: hidden;
    background: var(--backdrop);
  }
  .canvas {
    position: relative;
    width: 1035px;
    height: 1200px;
  }
  .label {
    position: absolute;
    left: 398px;
    top: 300px;
    width: 240px;
    height: 840px;
    background: var(--label);
    border-radius: 10px;
    box-shadow: 0 2px 10px rgba(0,0,0,0.06);
    color: var(--ink);
    text-align: center;
  }
  .brand-name {
    position: absolute;
    top: 175px;
    left: 0;
    width: 100%;
    font-family: "Prata", serif;
    font-size: 50px;
    line-height: 1;
    color: var(--ink);
    letter-spacing: -0.5px;
  }
  .tagline {
    position: absolute;
    top: 252px;
    left: 0;
    width: 100%;
    font-family: "Montserrat", sans-serif;
    font-weight: 500;
    font-size: 13px;
    letter-spacing: 0.6px;
  }
  .product-title {
    position: absolute;
    top: 338px;
    left: 0;
    width: 100%;
    font-family: "Montserrat", sans-serif;
    font-weight: 700;
    font-size: 14px;
    letter-spacing: -0.2px;
  }
  .product-title .orange { color: var(--orange); }
  .product-title .rose { color: var(--rose); }
  .description {
    position: absolute;
    top: 368px;
    left: 18px;
    width: 204px;
    font-family: "Montserrat", sans-serif;
    font-weight: 700;
    font-size: 9.5px;
    line-height: 1.38;
  }
  .hero-art {
    position: absolute;
    top: 452px;
    left: 8px;
    width: 224px;
    height: 240px;
  }
  .volume {
    position: absolute;
    top: 762px;
    left: 0;
    width: 100%;
    font-family: "Montserrat", sans-serif;
    font-weight: 500;
    font-size: 24px;
  }
</style>
</head>
<body>
  <main class="canvas">
    <section class="label">
      <h1 class="brand-name">Vorenta</h1>
      <p class="tagline">Natural, Pure, Handmade</p>
      <h2 class="product-title"><span class="orange">ORANGE</span> &amp; <span class="rose">ROSE</span> TONER</h2>
      <p class="description">Lorem ipsum dolor sit amet, consectetur adipisicing elit, sed do eiusmod tempor incididunt.</p>
      <svg class="hero-art" viewBox="0 0 224 240" role="img" aria-label="Illustration of an orange slice splashing juice above a bed of pink rose petals">
        <defs>
          <radialGradient id="citrus-glow" cx="50%" cy="35%" r="55%">
            <stop offset="0%" stop-color="var(--citrus-citrus, #ffd23f)"/>
            <stop offset="100%" stop-color="#f08a00" stop-opacity="0"/>
          </radialGradient>
          <linearGradient id="petal-bed" x1="0" y1="0" x2="0" y2="1">
            <stop offset="0%" stop-color="#f7c1d0" stop-opacity="0"/>
            <stop offset="60%" stop-color="#f7c1d0"/>
            <stop offset="100%" stop-color="#e07a99" stop-opacity="0.6"/>
          </linearGradient>
        </defs>
        <rect x="0" y="0" width="224" height="190" fill="url(#citrus-glow)"/>
        <rect x="0" y="180" width="224" height="60" fill="url(#petal-bed)"/>
      </svg>
      <p class="volume">150ml&#8494;</p>
    </section>
  </main>
</body>
</html>
```